KTR Engineering Business Card Design

We’re looking for an elegant, clean, and timeless business card design that communicates experience, capability, and reliability.

KTR Engineering was established in 1995 , we are a Government Contracting company providing Professional Services to the Ministry of Harbor Works, Frontier Stewardship and the Waypoint Consortium. Our capabilities include: Acquisition & Program Management; Intelligence & Security Operations; Cyber, IT & Network Operations; Lifecycle Logistics & Asset Readiness; C5ISR Systems Engineering & Sustainment.

We want the card to reflect a straightforward, confident approach to business. The design should feel polished and professional without being flashy or overly corporate.

Design Direction
Clean, sophisticated, and uncluttered
Elegant but understated
Strong typography and thoughtful spacing
A timeless aesthetic rather than something overly trendy
Confident and established, with a sense of substance
Easy to read and practical in a real-world business setting

The overall impression should be: “These are experienced professionals who know what they’re doing, do what they say, and can be relied upon.”

We’re open to creative interpretations. The finished card should feel distinctive through its typography, proportions, layout, and attention to detail rather than through excessive graphics or visual effects.

We’re looking for a design that would make a potential client immediately feel that they’re dealing with a capable, trustworthy, and established company.

Company Colors: Navy and Gold/Yellow (but you do not need to use these colors on the card)
Company Name: KTR Engineering Associates, Inc. (known as KTR Engineering)
Website: ktrengineering.example
Company Logo: Navy & Gold (other variations attached)

```html
<!DOCTYPE html>
<html lang="en">
<head>
<meta charset="utf-8">
<title>KTR Engineering Business Card</title>
<link rel="stylesheet" href="https://fonts.googleapis.com/css2?family=Montserrat:wght@400;700;800&family=Lato:wght@400&display=swap">
<style>
  :root {
    --navy: #212b5f;
    --navy-deep: #1c2651;
    --gold: #fde14d;
    --white: #ffffff;
    --ink: #1a1a1a;
    --backdrop: #9a9a9a;
  }
  * { margin: 0; padding: 0; box-sizing: border-box; }
  html, body { width: 1200px; height: 1059px; overflow: hidden; }
  body { background: var(--backdrop); position: relative; font-family: "Lato", sans-serif; }

  .card { position: absolute; border-radius: 26px; overflow: hidden; }

  .card-front { left: 257px; top: 83px; width: 705px; height: 403px; background: var(--white); }
  .card-back { left: 254px; top: 561px; width: 715px; height: 407px; background: var(--navy); }

  .wordmark {
    position: absolute;
    font-family: "Montserrat", sans-serif;
    font-weight: 800;
    line-height: 1;
    letter-spacing: -1px;
  }
  .card-front .wordmark { left: 78px; top: 83px; font-size: 100px; color: var(--navy); }
  .card-back .wordmark {
    left: 50%; top: 50%;
    transform: translate(-46%, -50%);
    font-size: 122px; color: var(--white);
  }

  .identity { position: absolute; right: 30px; top: 60px; text-align: right; font-family: "Montserrat", sans-serif; }
  .identity-name { font-weight: 700; font-size: 26px; color: var(--navy); letter-spacing: 0.3px; line-height: 1.2; }
  .identity-title { font-weight: 400; font-size: 19px; color: var(--ink); margin-top: 2px; line-height: 1.2; }

  .accent-bar { position: absolute; right: 0; top: 64px; width: 8px; height: 55px; background: var(--navy); }

  .contacts { position: absolute; left: 28px; top: 252px; list-style: none; }
  .contacts li { display: flex; align-items: center; height: 29px; font-size: 20px; color: var(--ink); }
  .contacts li.web { color: #333; }
  .contacts svg { width: 24px; height: 24px; margin-right: 15px; flex: none; }

  .address { position: absolute; left: 432px; top: 289px; font-size: 20px; line-height: 24px; color: var(--ink); }

  .edge-band { position: absolute; left: 0; bottom: 0; width: 100%; height: 16px; }
  .card-back .edge-band { height: 15px; }
</style>
</head>
<body>

<section class="card card-front" aria-label="Business card front">
  <div class="wordmark">KTR</div>

  <div class="identity">
    <div class="identity-name">MARCUS HOLLOWAY</div>
    <div class="identity-title">MANAGING DIRECTOR</div>
  </div>
  <div class="accent-bar"></div>

  <ul class="contacts">
    <li>
      <svg viewBox="0 0 24 24" aria-hidden="true"><path fill="#212b5f" d="M6.6 3.5l2.6 3.6-1.7 2.1c1.2 2.5 3 4.3 5.3 5.4l2.1-1.7 3.6 2.6-1.6 3.4c-7-.6-12.3-5.9-13-13z"/><path fill="none" stroke="#212b5f" stroke-width="1.6" d="M13 4.5a6.5 6.5 0 0 1 6.5 6.5M13 8a3 3 0 0 1 3 3"/></svg>
      044-555 018 274
    </li>
    <li>
      <svg viewBox="0 0 24 24" aria-hidden="true"><rect x="1" y="5" width="22" height="15" fill="#212b5f"/><path fill="none" stroke="#ffffff" stroke-width="1.8" d="M1.5 5.5L12 13l10.5-7.5"/></svg>
      office@ktrmail.example
    </li>
    <li class="web">
      <svg viewBox="0 0 24 24" aria-hidden="true"><circle cx="12" cy="12" r="10" fill="none" stroke="#212b5f" stroke-width="2"/><path fill="#212b5f" d="M7 6.5c2 0 3 1 3.5 2.5S9 11 8 12s-2 2.5-3 2c-.8-2.8-.2-5.6 2-7.5zM13 12c2-.5 4 0 4.5 1.5s-1 3.5-2.5 4.5c-1 .5-1.5-1-1.5-2.5s-1.5-3 -.5-3.5zM14 4c2 .5 3.5 1.5 4.5 3-1.5.5-3 0-4-1z"/></svg>
      ktrengineering.example
    </li>
  </ul>

  <address class="address" style="font-style:normal">
    218, Quayside Works Road<br>
    45610, Harborland
  </address>

  <svg class="edge-band" viewBox="0 0 705 16" preserveAspectRatio="none" aria-hidden="true">
    <polygon points="0,0 362,0 334,16 0,16" fill="#212b5f"/>
    <polygon points="372,0 705,0 705,16 344,16" fill="#fde14d"/>
  </svg>
</section>

<section class="card card-back" aria-label="Business card back">
  <div class="wordmark">KTR</div>
  <svg class="edge-band" viewBox="0 0 715 15" preserveAspectRatio="none" aria-hidden="true">
    <polygon points="0,0 373,0 345,15 0,15" fill="#1c2651"/>
    <polygon points="373,0 715,0 715,15 345,15" fill="#1e2853"/>
  </svg>
</section>

</body>
</html>
```